Business Card Design - Local Discount Club

Looking for a fun business card for a local discount club. One side should be the logo only and the other should be have :

Name
Title
Phone, Email
Website

```html
<!DOCTYPE html>
<html lang="en">
<head>
<meta charset="UTF-8">
<title>The Harbor Point Card – Business Card</title>
<link rel="stylesheet" href="https://fonts.googleapis.com/css2?family=Oswald:wght@600&family=Open+Sans:wght@400;600&display=swap">
<style>
  :root {
    --backdrop: #e8e5e0;
    --card: #1e1e1e;
    --wave-deep: #3b5cb8;
    --wave-sky: #3f9bd6;
    --wave-lime: #a7d46a;
    --name-blue: #3f8fd8;
    --ink-light: #e6e6e6;
  }
  * { margin: 0; padding: 0; box-sizing: border-box; }
  html, body {
    width: 1200px; height: 787px; overflow: hidden;
    background: var(--backdrop);
  }
  .stage {
    position: relative; width: 1200px; height: 787px;
    display: flex; align-items: center; justify-content: center; gap: 40px;
  }
  .card {
    position: relative; width: 540px; height: 309px;
    background: var(--card); border-radius: 16px; overflow: hidden;
    box-shadow: 0 10px 28px rgba(0,0,0,0.22);
  }
  .card-waves { position: absolute; left: 0; top: 0; width: 540px; height: 309px; }

  /* Front: contact side */
  .identity {
    position: absolute; right: 272px; top: 92px; text-align: right;
  }
  .identity-name {
    font-family: "Oswald", sans-serif; font-weight: 600;
    font-size: 36px; line-height: 1; letter-spacing: 0.5px;
    color: var(--name-blue); text-transform: uppercase;
  }
  .identity-title {
    font-family: "Open Sans", sans-serif; font-size: 14px;
    color: var(--ink-light); margin-top: 6px;
  }
  .divider {
    position: absolute; left: 284px; top: 96px; width: 1.5px; height: 66px;
    background: var(--wave-deep);
  }
  .contact-list {
    position: absolute; left: 300px; top: 98px; list-style: none;
    font-family: "Open Sans", sans-serif; font-size: 13.5px; color: var(--ink-light);
  }
  .contact-list li { display: flex; align-items: center; gap: 8px; height: 21px; }
  .contact-icon { width: 13px; height: 13px; flex: none; }

  /* Back: brand side */
  .brand {
    position: absolute; left: 0; right: 0; top: 96px;
    display: flex; align-items: center; justify-content: center; gap: 12px;
  }
  .brand-name {
    font-family: "Open Sans", sans-serif; font-weight: 600;
    font-size: 30px; color: var(--wave-sky); letter-spacing: 1px;
    text-transform: uppercase;
  }
  .brand-dot {
    width: 14px; height: 14px; border-radius: 50%; background: var(--wave-deep);
  }
</style>
</head>
<body>
<main class="stage">

  <section class="card card-front">
    <svg class="card-waves" viewBox="0 0 540 309" aria-hidden="true">
      <path d="M0,200 C140,206 300,262 540,276 L540,309 L0,309 Z" fill="var(--wave-sky)"/>
      <path d="M0,214 C150,222 280,300 540,300 L540,309 L0,309 Z" fill="var(--wave-deep)"/>
      <path d="M0,192 C140,196 300,252 540,268" fill="none" stroke="var(--wave-lime)" stroke-width="3"/>
    </svg>

    <div class="identity">
      <div class="identity-name">Dana Whitfield</div>
      <div class="identity-title">Owner</div>
    </div>
    <div class="divider"></div>
    <ul class="contact-list">
      <li>
        <svg class="contact-icon" viewBox="0 0 16 16"><path d="M4 1 L6.5 4.5 L5 6 C6 8.5 7.5 10 10 11 L11.5 9.5 L15 12 L13 15 C7 15 1 9 1 3 Z" fill="var(--name-blue)"/></svg>
        000.555.014.722
      </li>
      <li>
        <svg class="contact-icon" viewBox="0 0 16 16"><rect x="1" y="3" width="14" height="10" fill="none" stroke="var(--name-blue)" stroke-width="1.6"/><path d="M1 3 L8 9 L15 3" fill="none" stroke="var(--name-blue)" stroke-width="1.6"/></svg>
        hello@harborpointcard.com
      </li>
      <li>
        <svg class="contact-icon" viewBox="0 0 16 16"><circle cx="8" cy="8" r="6.5" fill="none" stroke="var(--name-blue)" stroke-width="1.4"/><ellipse cx="8" cy="8" rx="2.8" ry="6.5" fill="none" stroke="var(--name-blue)" stroke-width="1.2"/><line x1="1.5" y1="8" x2="14.5" y2="8" stroke="var(--name-blue)" stroke-width="1.2"/></svg>
        www.harborpointcard.com
      </li>
    </ul>
  </section>

  <section class="card card-back">
    <svg class="card-waves" viewBox="0 0 540 309" aria-hidden="true">
      <path d="M0,200 C140,206 300,262 540,276 L540,309 L0,309 Z" fill="var(--wave-sky)"/>
      <path d="M0,214 C150,222 280,300 540,300 L540,309 L0,309 Z" fill="var(--wave-deep)"/>
      <path d="M0,192 C140,196 300,252 540,268" fill="none" stroke="var(--wave-lime)" stroke-width="3"/>
    </svg>
    <div class="brand">
      <span class="brand-name">The Harbor Point Card</span>
      <span class="brand-dot"></span>
    </div>
  </section>

</main>
</body>
</html>
```